Financial Services Business Card Design

We are a financial services company Based in London, offering Short term Funding Solutions for companies, raising anywhere between £20,000 and £25million pounds.

The Card must have a professional look as it is going to be handed out to professionals I.E Solicitors, Accountants, Company directors and Business owners.

See Attached our company Logo

Industry/Entity Type

Business

Contact Information for Business Card

Lewis Thorncroft
Suite 41
R K House
Bramblecote Lane
Watford
HP19 4QX

```html
<!DOCTYPE html>
<html lang="en">
<head>
<meta charset="utf-8">
<title>Hartwell Funding Centre – Business Card</title>
<link rel="stylesheet" href="https://fonts.googleapis.com/css2?family=Open+Sans:wght@400;600;700&display=swap">
<style>
  :root {
    --backdrop: #e9e7e4;
    --blue-light: #3aa3dc;
    --blue-mid: #2a88cc;
    --blue-deep: #1560ad;
    --ink-grey: #6b6b6b;
    --ink-dark: #555555;
    --rule: #9a9a9a;
    --paper: #ffffff;
  }
  * { margin: 0; padding: 0; box-sizing: border-box; }
  html, body {
    width: 1200px; height: 800px; overflow: hidden;
    background: var(--backdrop);
    font-family: "Open Sans", Arial, sans-serif;
  }
  .stage {
    width: 1200px; height: 800px;
    display: flex; align-items: center; justify-content: center; gap: 60px;
  }
  .card { box-shadow: 0 6px 18px rgba(0,0,0,0.18); position: relative; overflow: hidden; }

  /* Front */
  .card-front {
    width: 320px; height: 560px;
    background: linear-gradient(160deg, var(--blue-light) 0%, var(--blue-mid) 55%, var(--blue-deep) 100%);
    display: flex; align-items: center; justify-content: center;
  }
  .front-brand {
    transform: rotate(90deg);
    display: flex; align-items: center; gap: 18px;
    white-space: nowrap;
  }
  .front-brand .brand-dot {
    width: 34px; height: 34px; border-radius: 50%; background: var(--paper);
  }
  .front-brand .brand-name {
    color: var(--paper); font-weight: 600; font-size: 30px; letter-spacing: 3px;
    text-transform: uppercase;
  }

  /* Back */
  .card-back {
    width: 560px; height: 320px; background: var(--paper);
  }
  .back-brand {
    position: absolute; left: 34px; top: 30px;
    display: flex; align-items: center; gap: 10px;
  }
  .back-brand .brand-dot { width: 16px; height: 16px; border-radius: 50%; background: var(--blue-mid); }
  .back-brand .brand-name {
    color: var(--blue-mid); font-weight: 600; font-size: 19px; letter-spacing: 2px;
    text-transform: uppercase;
  }
  .holder { position: absolute; left: 34px; top: 78px; }
  .holder-name { color: var(--blue-mid); font-weight: 700; font-size: 17px; text-transform: uppercase; letter-spacing: 0.5px; }
  .holder-role { color: var(--ink-grey); font-size: 11px; text-transform: uppercase; letter-spacing: 0.5px; margin-top: 2px; }
  .holder-rule { width: 250px; height: 1px; background: var(--rule); margin-top: 10px; }

  .contact-list { position: absolute; left: 34px; top: 150px; list-style: none; }
  .contact-list li {
    display: flex; align-items: center; gap: 8px;
    color: var(--ink-grey); font-size: 11.5px; line-height: 20px;
  }
  .contact-icon { width: 14px; height: 14px; flex: none; }

  .address {
    position: absolute; left: 34px; top: 222px;
    color: var(--ink-dark); font-weight: 700; font-size: 11.5px; line-height: 18px;
    text-transform: uppercase; font-style: normal; white-space: nowrap;
  }

  .growth-bars { position: absolute; right: 0; bottom: 0; width: 240px; height: 200px; }
</style>
</head>
<body>
<main class="stage">

  <section class="card card-front" aria-label="Card front">
    <div class="front-brand">
      <span class="brand-dot"></span>
      <span class="brand-name">Hartwell Funding</span>
    </div>
  </section>

  <section class="card card-back" aria-label="Card back">
    <div class="back-brand">
      <span class="brand-dot"></span>
      <span class="brand-name">Hartwell Funding</span>
    </div>

    <div class="holder">
      <p class="holder-name">Lewis Thorncroft</p>
      <p class="holder-role">Managing Director</p>
      <div class="holder-rule"></div>
    </div>

    <ul class="contact-list">
      <li>
        <svg class="contact-icon" viewBox="0 0 14 14" aria-hidden="true">
          <rect width="14" height="14" rx="2" fill="#2a88cc"/>
          <path d="M4 3.5 L5.6 3.5 L6.2 5.4 L5.2 6.1 Q6.1 7.9 7.9 8.8 L8.6 7.8 L10.5 8.4 L10.5 10 Q6.6 10.4 4 6.5 Z" fill="#fff"/>
        </svg>
        (020) 7946 0318
      </li>
      <li>
        <svg class="contact-icon" viewBox="0 0 14 14" aria-hidden="true">
          <rect width="14" height="14" rx="2" fill="#2a88cc"/>
          <rect x="3" y="4.2" width="8" height="5.6" fill="none" stroke="#fff" stroke-width="1"/>
          <path d="M3 4.4 L7 7.4 L11 4.4" fill="none" stroke="#fff" stroke-width="1"/>
        </svg>
        l.thorncroft@hartwellfunding.co.uk
      </li>
      <li>
        <svg class="contact-icon" viewBox="0 0 14 14" aria-hidden="true">
          <rect width="14" height="14" rx="2" fill="#2a88cc"/>
          <circle cx="7" cy="7" r="3.6" fill="none" stroke="#fff" stroke-width="1"/>
          <path d="M3.4 7 H10.6 M7 3.4 Q5 7 7 10.6 M7 3.4 Q9 7 7 10.6" fill="none" stroke="#fff" stroke-width="0.8"/>
        </svg>
        www.hartwellfunding.co.uk
      </li>
    </ul>

    <address class="address">
      Suite 41, R K House<br>
      Bramblecote Lane, Watford, HP19 4QX
    </address>

    <svg class="growth-bars" viewBox="0 0 240 200" aria-hidden="true">
      <rect x="12"  y="110" width="42" height="90"  fill="#3aa3dc"/>
      <rect x="70"  y="80"  width="42" height="120" fill="#2f94d3"/>
      <rect x="128" y="48"  width="42" height="152" fill="#2479bf"/>
      <rect x="186" y="12"  width="54" height="188" fill="#1560ad"/>
    </svg>
  </section>

</main>
</body>
</html>
```